KVT Trading Import Company web

We need a web design for an existing website we have. we want it to be simple yet flashy. It's a simple 3 page informative website with a link to our email address and line card. First page would be to introduce the company. second page would be the list of items we carry and third would be the contact page. I would like SEO optimization.
Updates
I would like a black background for the Webpage with flash and SEO optimization.
Reason: Need more information need it to be SEO
Industry/Entity Type
It Company
Look and feel
Each slider illustrates characteristics of the customer's brand and the style your logo design should communicate.

```html
<!DOCTYPE html>
<html lang="en">
<head>
<meta charset="utf-8">
<title>KVT Trading – Home</title>
<meta name="description" content="KVT Trading Import Company supplies construction materials, computers and trucks.">
<link href="https://fonts.googleapis.com/css2?family=Roboto:wght@300;400;500&display=swap" rel="stylesheet">
<style>
  :root{
    --page-bg:#1d5068;
    --bar-top:#3a3a3a;
    --bar-bottom:#0e0e0e;
    --white:#ffffff;
    --ink:#111111;
    --body-ink:#333333;
    --footer:#1a1a1a;
    --hero-a:#6b6e72;
    --hero-b:#2a2c2f;
  }
  *{margin:0;padding:0;box-sizing:border-box}
  html,body{width:1200px;height:869px;overflow:hidden}
  body{background:var(--page-bg);font-family:"Roboto",Arial,sans-serif;position:relative}
  .top-bar{position:absolute;left:0;top:0;width:1200px;height:49px;
    background:linear-gradient(var(--bar-top),var(--bar-bottom))}
  .page{position:absolute;left:131px;top:49px;width:913px;height:751px;background:var(--white)}
  .brand{position:absolute;left:187px;top:0;width:198px;height:144px;background:var(--white);
    box-shadow:0 2px 8px rgba(0,0,0,.45);display:flex;align-items:center;justify-content:center;gap:8px;z-index:3}
  .brand-dot{width:14px;height:14px;border-radius:50%;background:#1d5068}
  .brand-name{font-size:24px;font-weight:500;color:var(--ink)}
  .main-nav a{position:absolute;top:12px;font-size:17px;color:var(--white);text-decoration:none;font-weight:300}
  .main-nav .current{font-weight:400}
  .phone{position:absolute;left:875px;top:10px;display:flex;align-items:center;gap:9px;color:var(--white);font-size:17px}
  .hero{position:absolute;left:142px;top:58px;width:892px;height:432px;
    background:linear-gradient(135deg,var(--hero-a),var(--hero-b) 60%,#8a8d90)}
  .hero-title{position:absolute;right:40px;top:322px;font-size:47px;font-weight:300;color:var(--white)}
  .dots{position:absolute;top:392px;left:0;width:100%}
  .dot{position:absolute;width:14px;height:14px;border-radius:50%;background:var(--white)}
  .dot.hollow{background:transparent;border:2px solid var(--white)}
  .about{position:absolute;left:162px;top:519px;width:542px}
  .about h1{font-size:25px;font-weight:400;color:var(--ink);margin-bottom:10px}
  .about p{font-size:12.5px;line-height:22.6px;font-weight:300;color:var(--body-ink);text-align:justify}
  .category{position:absolute;left:729px;width:274px;height:60px;border-radius:3px;
    display:flex;align-items:center;font-size:24px;font-weight:300;color:var(--white);text-decoration:none}
  .category b{font-weight:500;margin-left:6px}
  .cat-materials{top:547px;padding-left:17px;background:linear-gradient(90deg,#3a3a3a,#151515)}
  .cat-computers{top:620px;padding-left:22px;background:linear-gradient(90deg,#7ba4cf,#3e6c9c 60%,#1e3a5a)}
  .cat-trucks{top:695px;padding-left:22px;background:linear-gradient(90deg,#222,#555 55%,#b0442a 78%,#9aa3aa)}
  .site-footer{position:absolute;left:130px;top:800px;width:915px;height:41px;background:var(--footer);
    color:var(--white);font-size:12.5px;font-weight:300;text-align:right;padding:13px 28px 0 0}
</style>
</head>
<body>
  <header>
    <div class="top-bar"></div>
    <div class="brand"><span class="brand-dot"></span><span class="brand-name">KVT Trading</span></div>
    <nav class="main-nav">
      <a class="current" href="#" style="left:427px">Home</a>
      <a href="#" style="left:519px">Our Services</a>
      <a href="#" style="left:668px">Contact us</a>
    </nav>
    <div class="phone">
      <svg width="28" height="28" viewBox="0 0 28 28" aria-hidden="true">
        <rect width="28" height="28" rx="4" fill="#fff"/>
        <path d="M10 6c-2 1-3 3-2 7s4 8 7 9c2 1 4 0 5-1l-3-3-2 1c-2-1-3-3-4-6l2-1-1-4z" fill="#222"/>
      </svg>
      <span>( 510 ) 555-0147</span>
    </div>
  </header>

  <main class="page"></main>

  <section class="hero" role="img" aria-label="Photo of two black semi trucks parked side by side">
    <div class="hero-title">Trucks</div>
    <div class="dots">
      <span class="dot" style="left:780px"></span>
      <span class="dot hollow" style="left:808px"></span>
      <span class="dot" style="left:835px"></span>
    </div>
  </section>

  <article class="about">
    <h1>About KVT Trading</h1>
    <p>Lorem Ipsum is simply dummy text of the printing and typesetting industry. Lorem Ipsum has been the industry's standard dummy text ever since the 1500s, when an unknown printer took a galley of type and scrambled it to make a type specimen book. It has survived not only five centuries, but also the leap into electronic typesetting, remaining essentially unchanged. It was popularised in the 1960s with the release of Letterline sheets containing Lorem Ipsum passages, and more recently with desktop publishing software like Folio PageCraft including versions of Lorem Ipsum. leap into electronic typesetting, remaining essentially unchanged. It was popularised in the 1960s with the release of Letterline sheets containing Lorem Ipsum passages, and more recently with desktop publishing software like Folio PageCraft including versions of Lorem Ipsum.</p>
  </article>

  <a class="category cat-materials" href="#" role="img" aria-label="Construction materials, steel rebar photo">Construction<b>materials</b></a>
  <a class="category cat-computers" href="#" role="img" aria-label="Computers, office workstation photo">Computers</a>
  <a class="category cat-trucks" href="#" role="img" aria-label="Trucks, photo of trucks">Trucks</a>

  <footer class="site-footer">© 2012 KVT Trading. All rights reserved.</footer>
</body>
</html>
```